Heronby Mortgage Capital Business Card

We need a business card design for our mortgage servicing company. In addition to servicing the loans of homeowners, we help homeowners with purchasing their homes and any mortgage refinancing. We would like to see designs that use the colors in the logo attached below (gold-ish yellow and navy blue), and any other design you deem fit! The design should communicate a simpler life with smart mortgages provided by Heronby.

```html
<!DOCTYPE html>
<html lang="en">
<head>
<meta charset="utf-8">
<title>Heronby Mortgage Capital – Business Card</title>
<link href="https://fonts.googleapis.com/css2?family=Montserrat:wght@400;700&display=swap" rel="stylesheet">
<style>
  :root {
    --backdrop: #559bb5;
    --card: #ffffff;
    --navy: #27244f;
    --gold: #deaf3b;
    --shadow: rgba(30, 60, 80, 0.45);
  }
  * { box-sizing: border-box; margin: 0; padding: 0; }
  html, body {
    width: 1008px; height: 1200px; overflow: hidden;
    background: var(--backdrop);
    font-family: "Montserrat", Arial, sans-serif;
  }
  .card {
    position: absolute; left: 114px; width: 776px; height: 444px;
    background: var(--card);
    box-shadow: 8px 10px 12px var(--shadow);
  }
  .card--front { top: 114px; }
  .card--back { top: 623px; }

  .holder { position: absolute; left: 49px; top: 42px; color: var(--navy); }
  .holder__name { font-size: 26px; font-weight: 400; letter-spacing: 0.3px; line-height: 1; }
  .holder__name strong { font-weight: 700; }
  .holder__role { font-size: 18px; font-weight: 400; margin-top: 3px; letter-spacing: 0.5px; }

  .contact { position: absolute; right: 46px; top: 40px; color: var(--navy); text-align: right; }
  .contact__row {
    display: flex; align-items: center; justify-content: flex-end;
    font-size: 24px; font-weight: 400; line-height: 30px; gap: 4px;
  }
  .contact__icon { width: 18px; height: 18px; flex: none; }

  .divider {
    position: absolute; left: 49px; right: 46px; top: 106px;
    height: 3px; background: var(--gold);
  }

  .brand {
    position: absolute; left: 0; right: 0;
    display: flex; align-items: center; justify-content: center; gap: 22px;
    color: var(--gold); font-weight: 700;
  }
  .card--front .brand { top: 222px; }
  .card--back .brand { top: 160px; }
  .brand__mark {
    width: 86px; height: 86px; border-radius: 50%;
    border: 3px solid var(--navy); flex: none;
  }
  .brand__text { text-align: center; line-height: 1; }
  .brand__name { display: block; font-size: 72px; letter-spacing: -1px; }
  .brand__sub { display: block; font-size: 24px; letter-spacing: 4px; margin-top: 6px; }
  .card--back .brand__name { font-size: 80px; }
  .card--back .brand__mark { width: 96px; height: 96px; }

  .website {
    position: absolute; left: 0; right: 0; top: 370px; text-align: center;
    color: var(--gold); font-size: 23px; font-weight: 400; letter-spacing: 13.5px;
  }
</style>
</head>
<body>
  <section class="card card--front">
    <div class="holder">
      <p class="holder__name"><strong>DANA</strong>WHITFIELD</p>
      <p class="holder__role">OWNER</p>
    </div>
    <div class="contact">
      <p class="contact__row">dana@heronbymail.com
        <svg class="contact__icon" viewBox="0 0 20 20" aria-hidden="true">
          <circle cx="10" cy="10" r="10" fill="var(--gold)"/>
          <rect x="5" y="6.5" width="10" height="7" rx="1" fill="#fff"/>
          <path d="M5.5 7 L10 10.5 L14.5 7" fill="none" stroke="var(--gold)" stroke-width="1.3"/>
        </svg>
      </p>
      <p class="contact__row">555-010-2234
        <svg class="contact__icon" viewBox="0 0 20 20" aria-hidden="true">
          <circle cx="10" cy="10" r="10" fill="var(--gold)"/>
          <path d="M7 5 L9 7.5 L8 9 Q9.5 11.5 11 12 L12.5 11 L15 13 L13.5 15 Q8 14.5 5.5 7 Z" fill="#fff"/>
        </svg>
      </p>
    </div>
    <div class="divider"></div>
    <div class="brand">
      <span class="brand__mark" aria-hidden="true"></span>
      <p class="brand__text"><span class="brand__name">Heronby</span><span class="brand__sub">MORTGAGE</span></p>
    </div>
  </section>

  <section class="card card--back">
    <div class="brand">
      <span class="brand__mark" aria-hidden="true"></span>
      <p class="brand__text"><span class="brand__name">Heronby</span><span class="brand__sub">MORTGAGE</span></p>
    </div>
    <p class="website">www.heronbymortgage.com</p>
  </section>
</body>
</html>
```